Modern Web Design for Nonprofit Organization

Our client is looking to redesign their website. They want a modern look, clean and professional, that integrates their new brand guidelines.

Here is clients current site:
http://www.valorandes.org/

They want their own unique design but here are some sites the clients likes:
https://www.brixtonvane.com/en/
https://oakhollowrise.org/
https://www.lumacraft.com/
https://www.tbnlawgroup.com/
https://www.greyharborco.org/

Attached please find the clients logos, color palette, site plan and design specs.

You will create a homepage mockup that will have the following sections in this order:
1. Thin Alert Bar at very top with one line message
2. Nav Bar with Logo and Main Nav (red in site plan)
3. Hero Image or Video
4. Signup Bar with name email and zip and connect button
5. Intro section with image, welcome message, and supporter counter
6. Featured Action section with call to action
7. Event section with two upcoming event cards
8. Latest News section with three latest blog post
9. Support our work (donation) section
10. Worker and Member Stories Section with feed of social posts
11. Footer.

You can use text and images from clients existing site or placeholder images and placeholder text.

Please submit as many home page mockups/idea boards as you like. Client will pick the top three and ask for some revisions. If you are selected this will lead to a lot of work for this client.

Project is private please adhere to ArtPlenary terms of use and do not share any materials please.

QUICKEST RESPONSE PLEASE!

Thanks for looking!

Target Market(s)

Non profit donors and farmworker advocates

Number of Pages Required

2 page

Font styles to use
Sans Serif

Requirements
Must have
• Adhere to brief and client brand ID
Nice to have
• World class design

```html
<!DOCTYPE html>
<html lang="es">
<head>
<meta charset="utf-8">
<title>Valor Andes Foundation — Home</title>
<link href="https://fonts.googleapis.com/css2?family=Montserrat:ital,wght@0,300;0,400;0,500;0,600;0,700;1,400&display=swap" rel="stylesheet">
<style>
:root{
  --red:#d90f0f;
  --black:#050505;
  --white:#ffffff;
  --stage:#f2f2f2;
  --grey-band:#e6e6e6;
  --lavender:#efeaf4;
  --navy:#2b2550;
  --text:#222;
  --muted:#555;
}
*{margin:0;padding:0;box-sizing:border-box}
html,body{width:1200px;height:3529px;overflow:hidden}
body{background:var(--stage);font-family:'Montserrat',sans-serif;color:var(--text);position:relative}
.page{position:absolute;left:137px;top:86px;width:925px;height:3177px;background:var(--white);overflow:hidden;box-shadow:0 30px 60px rgba(0,0,0,.18)}
.abs{position:absolute}
.center{text-align:center;left:0;right:0}

.alert-bar{top:0;left:0;width:925px;height:14px;background:var(--red);color:#fff;font-size:7px;line-height:14px;text-align:center}

.hero{top:14px;left:0;width:925px;height:440px;background:linear-gradient(180deg,#7fa6cf 0%,#a9c3dc 28%,#8a9a7a 45%,#4d6b35 70%,#2f4a22 100%)}
.hero-cut{top:400px;left:0;width:925px;height:60px}
.brand{top:34px;left:76px;display:flex;align-items:center;gap:8px}
.brand-dot{width:34px;height:34px;border-radius:50%;background:var(--red)}
.brand-name{font-weight:700;font-size:12px;line-height:13px;color:var(--black)}
.main-nav{top:44px;left:400px;display:flex;gap:22px;font-size:7px;font-weight:600;color:#111}
.lang-btn{top:38px;left:800px;width:50px;height:18px;border:1px solid var(--red);color:var(--red);font-size:7px;text-align:center;line-height:16px}
.hero-title{top:150px;left:490px;width:310px;text-align:center;color:#fff;font-size:31px;line-height:38px;font-weight:300}
.hero-title b{font-weight:700}
.cta-btn{top:280px;left:562px;width:98px;height:22px;border-radius:11px;background:var(--red);color:#fff;font-size:8px;font-weight:600;text-align:center;line-height:22px}

.signup{top:448px;left:137px;width:641px;height:301px}
.signup-text{top:0;left:137px;width:641px;color:#fff;text-align:center}
.signup h2{position:absolute;top:526px;left:0;right:0;font-size:14px;font-weight:600;letter-spacing:.5px}
.signup-label{position:absolute;left:0;right:0;font-size:11px}
.email-field{top:574px;left:347px;width:235px;height:22px;background:#fff;border-radius:11px}
.email-field span{position:absolute;left:12px;top:0;font-size:7px;color:#999;line-height:22px}
.email-btn{top:574px;left:507px;width:75px;height:22px;border-radius:11px;background:var(--red);color:#fff;font-size:8px;text-align:center;line-height:22px}
.text-in{top:645px;font-size:14px;color:var(--red);font-weight:500}
.fine{top:672px;font-size:6px;line-height:8px;color:#ddd}

.grey-block{background:var(--grey-band)}
.photo{border-radius:0}
.mission-kicker{top:776px;font-size:18px;color:var(--red)}
.mission-title{top:800px;font-size:18px;font-weight:700;color:var(--black)}
.mission-copy{top:838px;left:236px;width:464px;text-align:center;font-size:9px;line-height:14.3px;color:#333}

.features{top:1125px;left:0;width:925px;height:357px;background:var(--black)}
.sec-title{font-size:18px;font-weight:700;letter-spacing:.5px}
.sec-sub{font-size:7px}
.feature-card{top:1243px;width:171px;height:177px;background:#fff}
.feature-card .ph{height:107px}
.feature-card h3{font-size:9px;font-weight:700;text-align:center;margin-top:20px}
.feature-card p{font-size:7px;text-align:center;margin-top:8px;color:#444}
.feature-card i{position:absolute;bottom:0;left:60px;width:51px;height:4px;background:var(--red)}

.events{top:1482px;left:0;width:925px;height:356px;background:var(--lavender)}
.red-rule{width:70px;height:3px;background:var(--red);left:427px}
.event-card{top:1582px;width:182px;height:210px;background:#fff}
.event-card .ph{height:107px;position:relative}
.event-card .ph i{position:absolute;right:14px;bottom:-8px;width:17px;height:17px;border-radius:50%;background:var(--red)}
.event-card h4{font-size:8px;font-weight:700;margin:17px 0 0 18px}
.event-card .date{font-size:6px;color:var(--red);font-weight:600;margin:4px 0 0 18px}
.event-card .blurb{font-size:6px;color:#444;margin:5px 0 0 18px;width:130px;line-height:8px}
.event-card .more{position:absolute;left:18px;top:178px;width:48px;height:14px;background:var(--navy);color:#fff;font-size:6px;line-height:14px;text-align:center}

.news-card{top:1938px;width:185px;height:202px;background:#fff;box-shadow:0 2px 8px rgba(0,0,0,.12)}
.news-card .ph{height:82px}
.news-card h4{font-size:7.5px;font-weight:600;line-height:10px;margin:14px 26px 0}
.news-card .date{font-size:6.5px;color:var(--red);font-weight:600;margin:6px 26px 0}
.news-card p{font-size:6px;line-height:8px;color:#444;margin:6px 26px 0}

.logo-box{background:#fff;display:flex;align-items:center;justify-content:center}
.logo-box span{display:block;background:#a8a8a8}
.donate-pill{top:2264px;left:418px;width:86px;height:22px;border-radius:11px;background:var(--red);color:#fff;font-size:9px;font-weight:600;text-align:center;line-height:22px}

.board-card{top:2610px;width:251px;height:215px;background:#fff;box-shadow:0 2px 8px rgba(0,0,0,.12)}
.board-card blockquote{font-style:italic;font-size:9.5px;line-height:12px;color:#333;margin:28px 24px 0}
.board-card .avatar{position:absolute;left:24px;top:118px;width:82px;height:82px;border-radius:50%;background:linear-gradient(135deg,#7a5a48,#2b2320)}
.board-card .name{position:absolute;left:121px;top:140px;font-size:11px;font-weight:600;color:#111}
.board-card .role{position:absolute;left:121px;top:156px;font-size:6.5px;font-weight:600;color:var(--red)}
.board-card .socials{position:absolute;left:128px;top:172px;display:flex;gap:10px}
.board-card .socials i{width:9px;height:9px;border-radius:50%;border:1.5px solid #222}
.board-card .socials i:first-child{background:var(--red);border-color:var(--red)}

.footer{top:2877px;left:0;width:925px;height:300px;background:var(--black);color:#fff;text-align:center}
.footer h2{position:absolute;top:64px;left:0;right:0;font-size:16px;font-weight:600}
.donate-today{position:absolute;top:108px;left:407px;width:110px;height:22px;border:1.5px solid var(--red);border-radius:11px;font-size:8px;font-weight:600;line-height:19px;letter-spacing:.5px}
.footer-social{position:absolute;top:152px;left:0;right:0;display:flex;justify-content:center;gap:36px;font-size:9px;letter-spacing:1px}
.footer-phone{position:absolute;top:186px;left:0;right:0;font-size:8px;color:var(--red)}
.copyright{position:absolute;top:222px;left:0;right:0;font-size:6.5px}
</style>
</head>
<body>
<main class="page">

  <div class="abs alert-bar">New members: get your first 7 days of growing Premium for free! Click here to redeem</div>

  <header class="abs hero" role="img" aria-label="Woman in a hat holding a tablet, kneeling in a green farm field under blue sky"></header>
  <svg class="abs hero-cut" viewBox="0 0 925 60" preserveAspectRatio="none" aria-hidden="true">
    <path d="M0,60 L0,0 Q462,-24 925,0 L925,60 Z" fill="#fff"/>
  </svg>
  <div class="abs brand"><span class="brand-dot"></span><span class="brand-name">VALOR ANDES<br>FOUNDATION</span></div>
  <nav class="abs main-nav"><span>NOSOTROS</span><span>IMMIGRACION</span><span>UNETE</span><span>PROGRAMAS</span><span>BLOG</span><span>DONAR</span></nav>
  <div class="abs lang-btn">English</div>
  <h1 class="abs hero-title">Unete al<br><b>Movimiento</b><br>Campesino</h1>
  <div class="abs cta-btn">Call To Action</div>

  <svg class="abs signup" viewBox="0 0 641 301" aria-hidden="true">
    <path d="M0,0 Q20,301 330,301 Q560,290 641,0 Z" fill="#d90f0f"/>
    <path d="M8,0 Q30,292 330,292 Q555,282 641,0 Z" fill="#050505"/>
  </svg>
  <section class="signup" style="position:absolute;top:0;left:0;width:925px;color:#fff;text-align:center">
    <h2>MANTÉNGASE INFORMADO</h2>
    <p class="signup-label" style="top:547px">Inscribase con su Email</p>
    <div class="abs email-field"><span>✉ name@example.com</span></div>
    <div class="abs email-btn">Inscribase</div>
    <p class="signup-label" style="top:625px">Inscribase con su Numero de Teléfono</p>
    <p class="abs center text-in">Textea "PAPELES" al 555-010</p>
    <p class="abs center fine">La VAF nunca le cobrara por los mensajes por texto pero su compañía<br>de teléfono puede aplicarle cargos de acuerdo a su plan</p>
  </section>

  <div class="abs grey-block" style="left:0;top:843px;width:107px;height:277px"></div>
  <div class="abs grey-block" style="left:0;top:1028px;width:338px;height:92px"></div>
  <div class="abs grey-block" style="left:822px;top:843px;width:103px;height:277px"></div>
  <div class="abs grey-block" style="left:595px;top:1028px;width:330px;height:92px"></div>

  <p class="abs center mission-kicker">Mission</p>
  <h2 class="abs center mission-title">VALOR ANDES FOUNDATION</h2>
  <p class="abs mission-copy">The Valor Andes Foundation is a dynamic nonprofit organization established in 2006. The VAF Foundation's core purpose is to empower communities to ensure human dignity. We serve over 90,000 immigrants annually through a holistic approach; we provide critical services and engage our constituents in systemic change to break the cycle of poverty. Our regional offices are safe havens that provide resources and services—such as credible immigration legal advice—and act as hubs for educational outreach and organizing. In addition, our organization works to civically engage farmworkers and Latinos nationally in the democratic process by telling their story, voting and advocating for more equitable policies. The VAF Foundation also provides learning opportunities for members, community fellows, interns, and volunteers.</p>
  <div class="abs photo" style="left:158px;top:985px;width:95px;height:93px;background:linear-gradient(160deg,#a9b48a,#c62222)" role="img" aria-label="Smiling woman in a red shirt outdoors"></div>
  <div class="abs photo" style="left:338px;top:1001px;width:257px;height:119px;background:linear-gradient(120deg,#5e7a2e,#7a2440 55%,#4a6a25)" role="img" aria-label="Bunches of red grapes on the vine"></div>
  <div class="abs photo" style="left:708px;top:903px;width:161px;height:180px;background:linear-gradient(170deg,#c9b9a8,#8a6a5a 60%,#3a3e5a)" role="img" aria-label="People holding flags at a citizenship ceremony"></div>

  <section class="abs features">
    <h2 class="abs center sec-title" style="top:47px;color:#fff">FINIBUS BONORUM ET MALORUM</h2>
    <p class="abs center sec-sub" style="top:78px;color:#ddd">Sed ut perspiciatis unde omnis iste natus error sit voluptatem accusantium</p>
  </section>
  <article class="abs feature-card" style="left:104px"><div class="ph" style="background:linear-gradient(135deg,#9aa3ad,#3d4550)" role="img" aria-label="Volunteers handing out supplies"></div><h3>CENTRO DE RECURSOS</h3><p>Read More</p><i></i></article>
  <article class="abs feature-card" style="left:286px"><div class="ph" style="background:linear-gradient(135deg,#6f8f3a,#5a87b8)" role="img" aria-label="Farmworkers sharing a story under a vine"></div><h3>COMPARTE TU HISTORIA</h3><p>Read More</p><i></i></article>
  <article class="abs feature-card" style="left:468px"><div class="ph" style="background:linear-gradient(135deg,#d6c25a,#7a6a9a)" role="img" aria-label="Community members meeting at tables"></div><h3>EVENTOS CAMPESINOS</h3><p>Read More</p><i></i></article>
  <article class="abs feature-card" style="left:650px"><div class="ph" style="background:linear-gradient(135deg,#7d6a5a,#b33a3a)" role="img" aria-label="Speaker addressing reporters at a rally"></div><h3>NOTICIAS</h3><p>Read More</p><i></i></article>

  <section class="abs events"></section>
  <div class="abs red-rule" style="top:1520px"></div>
  <h2 class="abs center sec-title" style="top:1532px">UPCOMING EVENTS</h2>
  <article class="abs event-card" style="left:259px"><div class="ph" style="background:linear-gradient(160deg,#8a2a2a,#3a2a3a)" role="img" aria-label="Crowded conference hall audience"><i></i></div><h4>FINIBUS BONORUM</h4><p class="date">12 SEP 2020</p><p class="blurb">The standard Lorem Ipsum passage used since</p><span class="more">Read More</span></article>
  <article class="abs event-card" style="left:483px"><div class="ph" style="background:linear-gradient(160deg,#b0502a,#2a2f4a)" role="img" aria-label="Speaker in a suit presenting to an audience"><i></i></div><h4>FINIBUS BONORUM</h4><p class="date">12 SEP 2020</p><p class="blurb">The standard Lorem Ipsum passage used since</p><span class="more">Read More</span></article>

  <h2 class="abs center sec-title" style="top:1868px">FINIBUS BONORUM ET MALORUM</h2>
  <p class="abs center sec-sub" style="top:1898px;color:#444">Sed ut perspiciatis unde omnis iste natus error sit voluptatem accusantium</p>
  <article class="abs news-card" style="left:77px"><div class="ph" style="background:linear-gradient(120deg,#7fa06a,#d8e0cc)" role="img" aria-label="Two hands meeting in a handshake"></div><h4>Las Oficinas de la Fundacion VAF estaran Cerradas hasta Nuevo Aviso</h4><p class="date">April 22, 2020</p><p>Delano, California—Más de 1,000 comidas fueron distribuidas el miércoles en Delano a familias que sufren en medio</p></article>
  <article class="abs news-card" style="left:273px"><div class="ph" style="background:linear-gradient(160deg,#3f6a95,#2a4060)" role="img" aria-label="Eagle perched before mountains"></div><h4>Las Oficinas de la Fundacion VAF estaran Cerradas hasta Nuevo Aviso</h4><p class="date">April 22, 2020</p><p>Delano, California—Más de 1,000 comidas fueron distribuidas el miércoles en Delano a familias que sufren en medio</p></article>
  <article class="abs news-card" style="left:469px"><div class="ph" style="background:linear-gradient(160deg,#6a9ac8,#e6eef5)" role="img" aria-label="Hiker on a snowy mountain peak"></div><h4>Las Oficinas de la Fundacion VAF estaran Cerradas hasta Nuevo Aviso</h4><p class="date">April 22, 2020</p><p>Delano, California—Más de 1,000 comidas fueron distribuidas el miércoles en Delano a familias que sufren en medio</p></article>
  <article class="abs news-card" style="left:665px"><div class="ph" style="background:linear-gradient(160deg,#e0a060,#6a5a3a)" role="img" aria-label="Mother holding a child in a field at sunset"></div><h4>Las Oficinas de la Fundacion VAF estaran Cerradas hasta Nuevo Aviso</h4><p class="date">April 22, 2020</p><p>Delano, California—Más de 1,000 comidas fueron distribuidas el miércoles en Delano a familias que sufren en medio</p></article>

  <div class="abs grey-block" style="left:0;top:2233px;width:925px;height:274px"></div>
  <div class="abs" style="left:207px;top:2233px;width:520px;height:274px;background:#fff"></div>
  <div class="abs red-rule" style="top:2204px"></div>
  <h2 class="abs center sec-title" style="top:2222px">MOVIMIENTO CAMPESINO</h2>
  <div class="abs donate-pill">Donate Now</div>
  <div class="abs logo-box" style="left:112px;top:2233px;width:96px;height:89px"><span style="width:36px;height:36px;border-radius:50%"></span></div>
  <div class="abs logo-box" style="left:730px;top:2233px;width:90px;height:89px"><span style="width:58px;height:58px;border-radius:50%"></span></div>
  <div class="abs logo-box" style="left:215px;top:2327px;width:116px;height:83px;background:#f6f6f6"><span style="width:60px;height:34px"></span></div>
  <div class="abs logo-box" style="left:343px;top:2327px;width:117px;height:83px;background:#f6f6f6"><span style="width:44px;height:44px"></span></div>
  <div class="abs logo-box" style="left:471px;top:2327px;width:117px;height:83px;box-shadow:0 2px 8px rgba(0,0,0,.15)"><span style="width:70px;height:34px;background:#d90f0f"></span></div>
  <div class="abs logo-box" style="left:600px;top:2327px;width:115px;height:83px;background:#f6f6f6"><span style="width:66px;height:66px;border-radius:50%"></span></div>
  <div class="abs logo-box" style="left:343px;top:2417px;width:117px;height:83px;background:#f6f6f6"><span style="width:58px;height:58px;border-radius:50%"></span></div>
  <div class="abs logo-box" style="left:471px;top:2417px;width:117px;height:83px;background:#f6f6f6"><span style="width:80px;height:44px;border-radius:40px 40px 0 0"></span></div>

  <div class="abs red-rule" style="top:2548px"></div>
  <h2 class="abs center sec-title" style="top:2565px">BOARD MEMBERS</h2>
  <article class="abs board-card" style="left:77px"><blockquote>Lorem ipsum dolor sit amet, consectetur adipiscing elit, sed do eiusmod tempor incididunt ut labore et dolore magna aliqua. Quis ipsum suspendisse ultrices gravida. Risus commodo viverra maecenas accumsan lacus vel facilisis.</blockquote><div class="avatar" role="img" aria-label="Portrait of board member"></div><p class="name">ELENA MARQUEZ</p><p class="role">UNITED FIELD GROWERS</p><div class="socials"><i></i><i></i></div></article>
  <article class="abs board-card" style="left:337px"><blockquote>Lorem ipsum dolor sit amet, consectetur adipiscing elit, sed do eiusmod tempor incididunt ut labore et dolore magna aliqua. Quis ipsum suspendisse ultrices gravida. Risus commodo viverra maecenas accumsan lacus vel facilisis.</blockquote><div class="avatar" role="img" aria-label="Portrait of board member"></div><p class="name">ELENA MARQUEZ</p><p class="role">UNITED FIELD GROWERS</p><div class="socials"><i></i><i></i></div></article>
  <article class="abs board-card" style="left:597px"><blockquote>Lorem ipsum dolor sit amet, consectetur adipiscing elit, sed do eiusmod tempor incididunt ut labore et dolore magna aliqua. Quis ipsum suspendisse ultrices gravida. Risus commodo viverra maecenas accumsan lacus vel facilisis.</blockquote><div class="avatar" role="img" aria-label="Portrait of board member"></div><p class="name">ELENA MARQUEZ</p><p class="role">UNITED FIELD GROWERS</p><div class="socials"><i></i><i></i></div></article>

  <footer class="abs footer">
    <h2>Support Our Work!</h2>
    <div class="donate-today">DONATE TODAY</div>
    <div class="footer-social"><span>CHIRPLINE</span><span>PICTURELY</span><span>FRIENDSPACE</span></div>
    <p class="footer-phone">1-800-555-0142 Regional Office</p>
    <p class="copyright">Copyright © 2020 valorandesfoundation &nbsp;|&nbsp; All rights reserved.</p>
  </footer>

</main>
</body>
</html>
```